Specialized Personal Trainer Needs a Business Card Design

I need a business card design for my personal training business called Tall Pine Fitness. I have my Human Kinetics degree in Exercise Science from the Halvern Ridge College as well as an extra certification from NBKT (National Board of Kinetic Therapy). I work as a Cardiac Rehab Exercise Specialist and personal trainer giving specialized exercise prescriptions to those that have different heart conditions as well as work with the general population in weight loss, strength and conditioning, getting/staying fit.
Updates

I decided that I wanted a logo (as I did not have one before I submitted my project for a business card) so I am submitting a project to get a logo done and then I will decide on a business card, hopefully being able to use one of the designs already submitted.  My apologies for doing this backwards.  I am new to this so I appreciate your patience.

Thank you.

Hi, I have just created a project for a logo design (I realized I needed a logo and I should've done that first..oops!), please feel free to participate.  Once I receive a logo I like I will finalize my business card project and hopefully incorporate it into one of your business card designs. 

Thank you!

Target Market(s)

Business professionals

Industry/Entity Type

Personal Trainer

Requirements
Must have
• My name with my info:
Delia R. Whitcombe (BHK)
NBKT Certified Clinical Exercise Specialist & Personal Trainer
delia.whitcombe@tallpinefitness.example
Cell: 555-382-4170

Please make it double sided.
Nice to have
• An image that represents cardiac and general fitness training.

```html
<!DOCTYPE html>
<html lang="en">
<head>
<meta charset="utf-8">
<title>Delia R. Whitcombe – Business Card</title>
<link rel="stylesheet" href="https://fonts.googleapis.com/css2?family=Oswald:wght@700&family=Poiret+One&display=swap">
<style>
  :root {
    --brand-red: #d23a26;
    --ink: #111111;
    --paper: #ffffff;
  }
  html, body {
    margin: 0;
    padding: 0;
    width: 1200px;
    height: 686px;
    overflow: hidden;
    background: var(--paper);
  }
  .card {
    position: relative;
    width: 1200px;
    height: 686px;
    background: var(--paper);
    overflow: hidden;
  }
  .corner-accent {
    position: absolute;
    inset: 0;
    width: 1200px;
    height: 686px;
  }
  .corner-accent path { fill: var(--brand-red); }
  .identity {
    position: absolute;
    left: 0;
    right: 0;
    top: 188px;
    text-align: center;
  }
  .identity__name {
    margin: 0;
    font-family: "Oswald", "Arial Narrow", sans-serif;
    font-weight: 700;
    font-size: 50px;
    line-height: 1;
    color: var(--brand-red);
  }
  .identity__title {
    margin: 4px 0 0;
    font-family: "Poiret One", "Century Gothic", sans-serif;
    font-size: 49px;
    line-height: 40px;
    color: var(--ink);
    letter-spacing: 1px;
  }
  .contact {
    position: absolute;
    left: 167px;
    top: 467px;
    margin: 0;
    padding: 0;
    list-style: none;
  }
  .contact__item {
    display: flex;
    align-items: center;
    height: 70px;
    margin-bottom: 40px;
  }
  .contact__icon {
    width: 122px;
    height: 70px;
    flex: none;
  }
  .contact__icon path,
  .contact__icon rect,
  .contact__icon ellipse { fill: var(--brand-red); }
  .contact__text {
    margin-left: 12px;
    font-family: "Poiret One", "Century Gothic", sans-serif;
    font-size: 40px;
    color: var(--ink);
  }
</style>
</head>
<body>
<main class="card">
  <svg class="corner-accent" viewBox="0 0 1200 686" aria-hidden="true">
    <path d="M0 0 H178 C95 20 25 85 0 175 Z"/>
    <path d="M1200 686 H1040 C1120 650 1185 600 1200 540 Z"/>
  </svg>

  <header class="identity">
    <h1 class="identity__name">Delia R. Whitcombe (BHK)</h1>
    <p class="identity__title">NBKT Certified Clinical Exercise Specialist<br>&amp; Personal Trainer</p>
  </header>

  <ul class="contact">
    <li class="contact__item">
      <svg class="contact__icon" viewBox="0 0 122 70" aria-hidden="true">
        <path d="M0 0 H122 V70 H0 Z M8 6 L61 44 L114 6 Z M0 12 V64 L38 34 Z M122 12 V64 L84 34 Z M44 38 L6 70 H116 L78 38 L61 50 Z" fill-rule="evenodd"/>
      </svg>
      <span class="contact__text">delia.whitcombe@tallpinefitness.example</span>
    </li>
    <li class="contact__item">
      <svg class="contact__icon" viewBox="0 0 122 86" aria-hidden="true" style="height:86px">
        <path d="M4 18 C20 2 102 2 118 18 L118 30 L92 30 L90 20 C75 16 47 16 32 20 L30 30 L4 30 Z"/>
        <rect x="46" y="18" width="30" height="14" rx="3"/>
        <path d="M10 86 L22 40 C40 34 82 34 100 40 L112 86 Z"/>
        <ellipse cx="61" cy="60" rx="15" ry="13" fill="#ffffff" style="fill:#ffffff"/>
      </svg>
      <span class="contact__text">555-382-4170</span>
    </li>
  </ul>
</main>
</body>
</html>
```